Bellmore Roofing & construction LLC

I need an interactive website for potential customers with roofing products that we install and information about the products we install. I also want a page where customers can write reviews through google and facebook and can also contact us at. I would also like to add more information with the winning designer and would pay more with the winning designer.

```html
<!DOCTYPE html>
<html lang="en">
<head>
<meta charset="utf-8">
<title>Bellmore Roofing &amp; Construction LLC</title>
<link rel="stylesheet" href="https://fonts.googleapis.com/css2?family=Montserrat:wght@400;500;600;700;800&display=swap">
<style>
:root{
  --red:#ee1c25;
  --red-deep:#d4101a;
  --crimson:#e31d3c;
  --ink:#111111;
  --dark:#1c1c1e;
  --dark-2:#2a2a2c;
  --grey:#6d6d6d;
  --line:#9a9a9a;
  --white:#ffffff;
}
*{box-sizing:border-box;margin:0;padding:0}
html,body{width:1200px;height:5272px;overflow:hidden}
body{font-family:"Montserrat",sans-serif;color:var(--ink);background:var(--white);position:relative}
.abs{position:absolute}
.photo{position:absolute}
.wordmark{font-family:"Montserrat",sans-serif;font-weight:700;letter-spacing:2px;line-height:1.05}

/* header + hero */
.hero{position:absolute;left:0;top:0;width:1200px;height:720px;overflow:hidden}
.hero-bg{left:0;top:0;width:1200px;height:720px;background:linear-gradient(100deg,#2e2622 0%,#3b302a 40%,#5a4a40 60%,#8f8a86 100%)}
.hero-house{left:520px;top:150px;width:680px;height:520px;background:linear-gradient(160deg,#c9392b 0%,#b5302a 35%,#ece8e2 36%,#d9d4cc 100%)}
.hero-shade{left:0;top:0;width:1200px;height:720px;background:linear-gradient(90deg,rgba(0,0,0,.55),rgba(0,0,0,0) 55%)}
.site-logo{left:78px;top:22px;color:var(--white);font-size:26px}
.site-logo small{display:block;font-size:10px;letter-spacing:1.5px;font-weight:700;margin-top:4px}
.nav{right:190px;top:44px;display:flex;gap:26px;font-size:14px;color:var(--white);font-weight:500}
.nav a{color:inherit;text-decoration:none}
.nav a.active{color:var(--red);border-top:2px solid var(--red);padding-top:2px;margin-top:-4px}
.call-btn{left:1082px;top:34px;width:40px;height:40px;border-radius:50%;background:var(--red);display:flex;align-items:center;justify-content:center}
.eyebrow-red{left:78px;top:256px;color:var(--red);font-size:17px;font-weight:500}
.hero-title{left:78px;top:288px;color:var(--white);font-size:41px;font-weight:800;line-height:47px}
.cta{left:78px;top:442px;width:291px;height:62px;background:var(--red);color:var(--white);font-size:17px;font-weight:500;display:flex;align-items:center;justify-content:center}

/* about */
.about-name{left:84px;top:900px;font-size:40px;font-weight:700;color:var(--ink);letter-spacing:0}
.about-sub{left:88px;top:952px;font-size:12px;font-weight:700;color:var(--grey);letter-spacing:.5px}
.about-text{left:590px;top:756px;width:490px;font-size:13.5px;line-height:27px;color:var(--grey)}
.about-text p+p{margin-top:20px}
.about-house{left:225px;top:1020px;width:975px;height:395px;background:linear-gradient(90deg,rgba(255,255,255,0) 0%,#c96a4d 12%,#e4a27c 40%,#f0d8cc 70%,rgba(240,240,240,.4) 100%)}

/* services */
.services-bg{left:0;top:1390px;width:1200px;height:650px}
.sec-title{width:1200px;left:0;text-align:center}
.services-title{top:1552px;color:var(--white);font-size:39px;font-weight:700}
.services-lead{top:1616px;color:var(--white);font-size:16px;font-style:italic;line-height:27px}
.service-card{top:1720px;width:322px;height:385px;display:flex;align-items:flex-end;justify-content:center;padding-bottom:26px;color:var(--white);font-weight:700;font-size:19px;letter-spacing:.5px}
.card-roofing{left:94px;background:linear-gradient(180deg,#b8b6b1 0%,#8c7a62 55%,#3a2f28 100%)}
.card-remodel{left:438px;background:linear-gradient(180deg,#a9c2d8 0%,#c6d3dd 35%,#2c2f33 60%,#1a1c1e 100%)}
.card-construction{left:782px;background:linear-gradient(180deg,#c1c7cc 0%,#9a958e 35%,#5c4f43 70%,#2b2520 100%)}

/* testimonials */
.label{font-size:12px;font-weight:700;color:var(--grey);letter-spacing:.5px}
.h2{font-size:39px;font-weight:700;color:var(--ink)}
.avatar{left:528px;top:2369px;width:144px;height:144px;border-radius:50%;background:radial-gradient(circle at 50% 45%,#c99c80 0%,#7a5640 55%,#3a2a22 100%)}
.arrow-btn{top:2446px;width:52px;height:52px;border-radius:50%;display:flex;align-items:center;justify-content:center}
.arrow-prev{left:142px;border:2px solid var(--red)}
.arrow-next{left:996px;border:2px solid #e3e3e3}
.quote{top:2548px;left:290px;width:620px;text-align:center;font-size:13.5px;line-height:29px;color:var(--grey)}
.client-name{top:2668px;font-size:16px;font-weight:700}
.client-site{top:2695px;font-size:14px;color:var(--red)}

/* why choose */
.why-bg{left:0;top:2748px;width:1200px;height:740px}
.why-label{left:543px;top:2870px;color:#cfcfcf;font-size:12px;font-weight:700}
.why-title{left:543px;top:2898px;color:var(--white);font-size:39px;font-weight:700}
.feature{left:797px;width:330px;color:var(--white)}
.feature h3{font-size:15px;font-weight:700;margin-bottom:10px}
.feature p{font-size:13px;line-height:25px;color:#e4e4e4}
.feature-icon{left:630px}

/* projects */
.project-img{left:303px;top:3660px;width:594px;height:415px;background:linear-gradient(180deg,#dbe6ee 0%,#b77a5a 30%,#b9a27c 55%,#5f7a45 80%,#3f5a2f 100%)}

/* contact */
.contact-bg{left:0;top:4300px;width:1200px;height:560px;background:linear-gradient(180deg,#ffffff 0%,#f4f4f4 50%,#ececec 100%)}
.form-box{left:123px;top:4356px;width:954px;height:412px;border:3px solid #6e6e6e;background:rgba(255,255,255,.92)}
.field{position:absolute;width:392px;border-bottom:1.5px solid var(--line);font-size:13px;color:var(--grey);padding-bottom:20px}
.field.focus{border-color:var(--red);color:var(--red)}
.send-btn{left:965px;top:4626px;width:70px;height:70px;border-radius:50%;background:var(--red);display:flex;align-items:center;justify-content:center}

/* footer */
.footer-bg{left:0;top:4830px;width:1200px;height:442px}
.footer-logo{left:80px;top:4995px;color:var(--white);font-size:34px}
.footer-logo small{display:block;font-size:13px;letter-spacing:2px;margin-top:6px}
.social{top:5106px;width:42px;height:42px;border-radius:50%;border:2px solid var(--red)}
.foot-col h4{color:var(--white);font-size:16px;font-weight:700;margin-bottom:20px}
.foot-col ul{list-style:none}
.foot-col li{color:#dcdcdc;font-size:13.5px;line-height:29px;padding-left:20px;position:relative}
.foot-col li::before{content:"";position:absolute;left:0;top:12px;width:6px;height:6px;border-radius:50%;background:var(--red)}
.contact-row{display:flex;gap:16px;color:#dcdcdc;font-size:13.5px;line-height:25px;margin-bottom:20px}
.contact-row svg{flex:none;margin-top:4px}
.copyright{top:5232px;color:#dcdcdc;font-size:13px}
</style>
</head>
<body>

<!-- Hero -->
<header class="hero">
  <div class="abs hero-bg" role="img" aria-label="Dark shingled roof background"></div>
  <div class="abs hero-house" role="img" aria-label="White house with red tiled roof"></div>
  <div class="abs hero-shade"></div>
  <svg class="abs" style="left:0;top:0" width="1200" height="720" viewBox="0 0 1200 720">
    <polygon points="0,690 1200,628 1200,720 0,720" fill="#ffffff"/>
    <polygon points="0,690 1200,628 1200,646 0,720" fill="#ee1c25"/>
  </svg>
  <div class="abs site-logo wordmark">BELLMORE ROOFING<small>&amp; CONSTRUCTION LLC</small></div>
  <nav class="abs nav">
    <a class="active" href="#">HOME</a><a href="#">ABOUT</a><a href="#">SERVICES</a><a href="#">PROJECTS</a><a href="#">TESTIMONIALS</a><a href="#">CONTACT</a>
  </nav>
  <div class="abs call-btn">
    <svg width="18" height="18" viewBox="0 0 24 24"><path d="M6.6 10.8a15 15 0 0 0 6.6 6.6l2.2-2.2a1 1 0 0 1 1-.25 11.4 11.4 0 0 0 3.6.57 1 1 0 0 1 1 1V20a1 1 0 0 1-1 1A17 17 0 0 1 3 4a1 1 0 0 1 1-1h3.5a1 1 0 0 1 1 1c0 1.25.2 2.45.57 3.57a1 1 0 0 1-.25 1z" fill="#fff"/></svg>
  </div>
  <div class="abs eyebrow-red">High Quality Work</div>
  <h1 class="abs hero-title">WE WILL HELP<br>YOU TO FIX YOUR<br>ROOF</h1>
  <div class="abs cta">GET FREE CONSULTATION</div>
</header>

<!-- About -->
<section>
  <div class="abs about-name">BELLMORE ROOFING</div>
  <div class="abs about-sub">&amp; CONSTRUCTION LLC</div>
  <div class="abs about-text">
    <p>Lorem Ipsum is simply dummy text of printing and typesetting industry. Lorem Ipsum has been the industry's standard dummy text ever since the 1500s, when an unknown Lorem Ipsum is simply dummy text of printing and typesetting industry Lorem Ipsum is simply dummy.</p>
    <p>Lorem Ipsum is simply dummy text of printing and typesetting industry. Lorem Ipsum has been the industry's standard dummy text ever since the 1500s,</p>
  </div>
  <div class="abs about-house" role="img" aria-label="Two-storey peach house with red tiled roof and balconies"></div>
</section>

<!-- Services -->
<section>
  <svg class="abs services-bg" viewBox="0 0 1200 650" width="1200" height="650" role="img" aria-label="Red tinted background of roofers at work">
    <defs><linearGradient id="svcGrad" x1="0" y1="0" x2="1" y2="1"><stop offset="0" stop-color="#e8243f"/><stop offset="1" stop-color="#d11a2e"/></linearGradient></defs>
    <polygon points="0,66 1200,0 1200,560 0,630" fill="url(#svcGrad)"/>
  </svg>
  <h2 class="abs sec-title services-title">OUR SERVICES</h2>
  <p class="abs sec-title services-lead">Lorem Ipsum is simply dummy text of printing and typesetting industry<br>Lorem Ipsum has been the industry's standard.</p>
  <div class="abs service-card card-roofing" role="img" aria-label="Roofers framing a roof">ROOFING</div>
  <div class="abs service-card card-remodel" role="img" aria-label="Dark tiled roof against sky">REMODELING</div>
  <div class="abs service-card card-construction" role="img" aria-label="Roof under construction with ladders">CONSTRUCTION</div>
</section>

<!-- Testimonials -->
<section>
  <div class="abs sec-title label" style="top:2263px">TESTIMONIALS</div>
  <h2 class="abs sec-title h2" style="top:2290px">WHAT OUR CLIENT SAY</h2>
  <div class="abs avatar" role="img" aria-label="Client portrait"></div>
  <div class="abs arrow-btn arrow-prev"><svg width="14" height="22" viewBox="0 0 14 22"><path d="M11 2 2 11l9 9" fill="none" stroke="#ee1c25" stroke-width="2"/></svg></div>
  <div class="abs arrow-btn arrow-next"><svg width="14" height="22" viewBox="0 0 14 22"><path d="m3 2 9 9-9 9" fill="none" stroke="#dcdcdc" stroke-width="2"/></svg></div>
  <p class="abs quote">Lorem Ipsum is simply dummy text of the printing and typesetting industry. Lorem Ipsum has been the industry's standard dummy Lorem Ipsum is simply dummy text of the printing and.</p>
  <div class="abs sec-title client-name">CLIENT NAME</div>
  <div class="abs sec-title client-site">Something.com</div>
</section>

<!-- Why choose -->
<section>
  <svg class="abs why-bg" viewBox="0 0 1200 740" width="1200" height="740">
    <defs><linearGradient id="whyGrad" x1="0" y1="0" x2="1" y2="0"><stop offset="0" stop-color="#3a3634"/><stop offset="1" stop-color="#1c1c1e"/></linearGradient></defs>
    <polygon points="0,80 1200,0 1200,640 0,740" fill="url(#whyGrad)"/>
    <polygon points="0,690 1200,630 1200,640 0,740" fill="#ee1c25"/>
    <polygon points="150,70 0,340 0,740 660,640" fill="#ee1c25"/>
    <polygon points="160,100 20,360 20,720 640,628" fill="#c7c4be" role="img" aria-label="Roofer on a ladder measuring a house wall"/>
    <polygon points="656,198 606,282 706,282" fill="#8e1a1e" opacity=".8"/>
    <polygon points="700,376 650,460 750,460" fill="#8e1a1e" opacity=".8"/>
  </svg>
  <div class="abs why-label">WHY CHOOSE</div>
  <h2 class="abs why-title">BELLMORE ROOFING</h2>
  <div class="abs feature" style="top:3012px"><h3>INSTALL</h3><p>Lorem Ipsum is simply dummy text of printing and typesetting industry.</p></div>
  <div class="abs feature" style="top:3188px"><h3>INFORMATION</h3><p>Lorem Ipsum is simply dummy text of printing and typesetting industry.</p></div>
</section>

<!-- Projects -->
<section>
  <div class="abs sec-title label" style="top:3546px">OUR WORKS</div>
  <h2 class="abs sec-title h2" style="top:3572px">OUR PROJECTS</h2>
  <svg class="abs" style="left:0;top:3655px" width="1200" height="425" viewBox="0 0 1200 425">
    <polygon points="0,120 277,0 277,425 0,340" fill="#ee1c25"/>
    <polygon points="922,0 1200,110 1200,330 922,425" fill="#ee1c25"/>
    <polygon points="226,212 250,190 250,234" fill="#111"/>
    <line x1="206" y1="212" x2="232" y2="212" stroke="#ee1c25" stroke-width="2"/>
    <polygon points="952,180 1002,212 952,244" fill="none" stroke="#fff" stroke-width="2"/>
    <line x1="960" y1="212" x2="985" y2="212" stroke="#fff" stroke-width="2"/>
  </svg>
  <div class="abs project-img" role="img" aria-label="Stone house with red tiled roof and garden"></div>
</section>

<!-- Contact -->
<section>
  <div class="abs contact-bg" role="img" aria-label="Faded house background"></div>
  <div class="abs sec-title label" style="top:4242px">STAY CONNETED</div>
  <h2 class="abs sec-title h2" style="top:4268px">CONTACT US</h2>
  <form class="abs form-box">
    <div class="field focus" style="left:60px;top:66px">Name *</div>
    <div class="field" style="left:498px;top:66px">Email *</div>
    <div class="field" style="left:60px;top:160px">Phone*</div>
    <div class="field" style="left:498px;top:160px">Message *</div>
    <div class="field" style="left:60px;top:262px">Services *</div>
    <div class="field" style="left:498px;top:262px">&nbsp;</div>
  </form>
  <div class="abs send-btn"><svg width="26" height="26" viewBox="0 0 24 24"><path d="M22 2 2 10l8 3 3 8z" fill="#fff"/><path d="M22 2 10 13" stroke="#ee1c25" stroke-width="1.5"/></svg></div>
</section>

<!-- Footer -->
<footer>
  <svg class="abs footer-bg" viewBox="0 0 1200 442" width="1200" height="442">
    <polygon points="0,18 1200,78 1200,442 0,442" fill="#1c1c1e"/>
    <polygon points="0,0 1200,70 1200,86 0,28" fill="#ee1c25"/>
  </svg>
  <div class="abs footer-logo wordmark">BELLMORE<small>ROOFING &amp; CONSTRUCTION</small></div>
  <div class="abs social" style="left:122px"></div>
  <div class="abs social" style="left:174px"></div>
  <div class="abs foot-col" style="left:346px;top:4946px">
    <h4>SITEMAP</h4>
    <ul><li>Home</li><li>About</li><li>Services</li><li>Projects</li><li>Testimonials</li><li>Contact</li></ul>
  </div>
  <div class="abs foot-col" style="left:612px;top:4946px">
    <h4>SERVICES</h4>
    <ul><li>Roofing</li><li>Remodeling</li><li>Construction</li></ul>
  </div>
  <div class="abs foot-col" style="left:879px;top:4946px;width:260px">
    <h4>CONTACT US</h4>
    <div class="contact-row"><svg width="18" height="22" viewBox="0 0 18 22"><path d="M9 1a7 7 0 0 0-7 7c0 5 7 13 7 13s7-8 7-13a7 7 0 0 0-7-7z" fill="none" stroke="#ee1c25" stroke-width="2"/><circle cx="9" cy="8" r="2.5" fill="#ee1c25"/></svg><span>Bellmore<br>101 - Ipsum simple text<br>print type industry.</span></div>
    <div class="contact-row"><svg width="18" height="18" viewBox="0 0 24 24"><path d="M6.6 10.8a15 15 0 0 0 6.6 6.6l2.2-2.2a1 1 0 0 1 1-.25 11.4 11.4 0 0 0 3.6.57 1 1 0 0 1 1 1V20a1 1 0 0 1-1 1A17 17 0 0 1 3 4a1 1 0 0 1 1-1h3.5a1 1 0 0 1 1 1c0 1.25.2 2.45.57 3.57a1 1 0 0 1-.25 1z" fill="#ee1c25"/></svg><span>123 456 7890</span></div>
    <div class="contact-row"><svg width="18" height="16" viewBox="0 0 18 16"><rect x="0" y="1" width="18" height="14" fill="#ee1c25"/><path d="m1 2 8 7 8-7" fill="none" stroke="#1c1c1e" stroke-width="1.5"/></svg><span>info@bellmore.com</span></div>
  </div>
  <div class="abs sec-title copyright">©Bellmore Roofing -2020 All rights reserved.</div>
</footer>

</body>
</html>
```